Website design with eCommerce for revolutionary new product in the manufacturing industry.

We need a website designed for a precision manufacturing company based in the suburbs of Minneapolis, Minnesota called Velk Manufacturing. We have a revolutionary new product, the TREMLA, to introduce and sell through an eCommerce storefront. The website would include company information, product information, and the storefront. Green is a color that represents Velk Manufacturing. The final design should communicate that we exclusively offer premium products at a premium price. The design should also let the customer know they are the focus of our work.

Target Market(s)

Machinists and machine shops

Industry/Entity Type

Manufacturing and machine shops

Coding

Coded - Design and coding required

Font styles to use
Sans Serif

Colors
59FF00
82FF00
B8FF75
E3FFCB
F4FFEA

Requirements
Must have
• eCommerce storefront, Made in USA references
Nice to have
• Home page, TREMLA Product page, About Us, Capabilities, Contact, etc.
Should not have
• Should not be too much text and reading.

```html
<!DOCTYPE html>
<html lang="en">
<head>
<meta charset="utf-8">
<title>Velk Manufacturing</title>
<link href="https://fonts.googleapis.com/css2?family=Rajdhani:wght@500;600;700&family=Roboto:wght@400;500;700&display=swap" rel="stylesheet">
<style>
:root{
  --green:#59FF00;
  --lime:#82FF00;
  --mint:#B8FF75;
  --pale:#E3FFCB;
  --paler:#F4FFEA;
  --ink:#1b1b1b;
  --text:#444;
  --muted:#777;
  --dark:#0d0d0d;
  --line:#e3e3e3;
}
*{box-sizing:border-box;margin:0;padding:0}
html,body{width:1200px;height:4004px;overflow:hidden}
body{font-family:"Roboto",sans-serif;color:var(--text);background:#fff;position:relative}
.heading{font-family:"Rajdhani",sans-serif;font-weight:700;color:var(--ink);text-transform:uppercase;letter-spacing:1px}

/* header */
.site-header{position:absolute;top:0;left:0;width:1200px;height:124px;background:#fff}
.topbar{position:absolute;right:0;top:0;width:680px;height:34px;background:var(--lime);clip-path:polygon(4% 0,100% 0,100% 100%,0 100%);display:flex;justify-content:flex-end;align-items:center;gap:26px;padding-right:112px;font-size:13px;color:var(--ink);font-weight:500}
.topbar span{display:flex;align-items:center;gap:6px}
.brand{position:absolute;left:112px;top:30px;font-family:"Rajdhani",sans-serif;font-weight:700;font-size:30px;color:var(--ink);display:flex;align-items:center;gap:10px;text-transform:uppercase}
.brand .dot{width:18px;height:18px;background:var(--green);border-radius:50%}
.main-nav{position:absolute;right:112px;top:70px;display:flex;gap:34px;font-size:15px;font-weight:500;color:var(--ink)}

/* hero */
.hero{position:absolute;top:124px;left:0;width:1200px;height:700px;overflow:hidden}
.hero-photo{position:absolute;inset:0;background:radial-gradient(ellipse at 50% 40%,#4a4a4a 0%,#262626 45%,#111 100%)}
.hero-content{position:absolute;top:150px;left:0;width:100%;text-align:center}
.hero-title{font-family:"Rajdhani",sans-serif;font-weight:700;color:var(--green);text-transform:uppercase;line-height:.95}
.hero-title .line1{display:block;font-size:150px;letter-spacing:8px}
.hero-title .line2{display:block;font-size:88px;letter-spacing:3px;margin-top:10px}
.btn-green{display:inline-block;background:var(--green);color:var(--ink);font-weight:700;font-size:14px;padding:16px 30px;border-radius:28px;text-transform:uppercase;margin-top:34px}
.hero-wave{position:absolute;bottom:0;left:0}
.hero-dots{position:absolute;bottom:70px;left:0;width:100%;display:flex;justify-content:center;gap:10px}
.hero-dots i{width:12px;height:12px;border-radius:50%;background:#fff;opacity:.7}
.hero-dots i.on{opacity:1;background:var(--paler)}

/* why */
.why{position:absolute;top:860px;left:0;width:1200px;text-align:center}
.section-title{font-size:34px}
.why p.lead{width:560px;margin:26px auto 0;font-size:17px;line-height:1.65;color:var(--text)}
.why-cards{display:flex;justify-content:center;gap:36px;margin-top:50px}
.why-card{width:304px;height:252px;border-radius:26px 4px 26px 4px;background:linear-gradient(180deg,var(--lime),var(--mint));display:flex;flex-direction:column;align-items:center;justify-content:center;gap:26px;padding:0 40px}
.why-card .icon{width:78px;height:78px;border-radius:50%;background:#fff;display:flex;align-items:center;justify-content:center}
.why-card p{font-size:16px;line-height:1.5;color:var(--ink)}

/* products */
.featured{position:absolute;top:1360px;left:0;width:1200px;text-align:center}
.sub{font-size:14px;color:var(--muted);margin-top:14px}
.product-row{display:flex;justify-content:center;gap:22px;margin-top:40px;position:relative}
.product-card{width:228px;height:372px;border:1px solid var(--line);background:#fff;padding:10px}
.product-photo{height:196px;background:linear-gradient(135deg,#6b6b6b,#b89a6a 55%,#3a3a3a)}
.product-photo.b{background:linear-gradient(135deg,#2c2c2c,#9a9a9a 50%,#1f1f1f)}
.product-photo.c{background:linear-gradient(135deg,#3a3a3a,#4fbf1a 50%,#222)}
.product-photo.d{background:linear-gradient(135deg,#2a3c6a,#c0893d 50%,#1b2a4a)}
.stars{color:#f0a500;font-size:16px;letter-spacing:2px;margin-top:16px}
.product-name{font-size:18px;margin-top:8px}
.btn-outline{display:inline-block;margin-top:16px;border:1px solid #bbb;border-radius:20px;padding:9px 22px;font-size:11px;font-weight:700;color:var(--ink);text-transform:uppercase}
.arrow{position:absolute;top:150px}
.arrow.left{left:48px}
.arrow.right{right:48px}

/* process band */
.process{position:absolute;top:1932px;left:0;width:1200px;height:590px;background:linear-gradient(180deg,var(--mint),var(--lime) 45%,var(--mint))}
.process-photo{position:absolute;left:150px;top:60px;width:440px;height:420px;border-radius:8px;background:linear-gradient(135deg,rgba(20,60,0,.35),rgba(89,255,0,.5) 50%,rgba(40,40,40,.35))}
.process-body{position:absolute;left:640px;top:90px;width:440px}
.process-body h2{font-size:36px}
.process-body .rule{width:70px;height:3px;background:var(--ink);margin:12px 0 26px}
.process-body ul{list-style:none}
.process-body li{position:relative;padding-left:28px;font-size:14px;line-height:1.55;color:var(--ink);margin-bottom:16px}
.process-body li::before{content:"";position:absolute;left:2px;top:5px;width:11px;height:11px;border-radius:50%;background:var(--ink)}

/* gallery */
.gallery{position:absolute;top:2580px;left:0;width:1200px;text-align:center}
.gallery-grid{display:grid;grid-template-columns:repeat(3,316px);gap:14px;justify-content:center;margin-top:40px}
.gallery-grid div{height:232px}
.g1{background:radial-gradient(circle,#8a8a8a,#4a4a4a)}
.g2{background:linear-gradient(135deg,#5a5a5a,#c7b08a,#6a6a6a)}
.g3{background:linear-gradient(135deg,#1f2c4f,#5a7ab5,#10182f)}
.g4{background:linear-gradient(135deg,#2a3a6a,#c99048,#1e2a4c)}
.g5{background:linear-gradient(135deg,#2a2a2a,#8f8f8f,#1a1a1a)}
.g6{background:linear-gradient(135deg,#3a3a3a,#d9d9d9,#2c2c2c)}

/* capabilities */
.capabilities{position:absolute;top:3210px;left:0;width:1200px;height:478px;background:linear-gradient(180deg,var(--lime) 0%,var(--mint) 35%,var(--paler) 100%);text-align:center;padding-top:110px}
.cap-grid{display:flex;justify-content:center;gap:30px;margin-top:40px}
.cap{width:220px}
.cap h3{font-size:18px;margin-top:12px}
.cap p{font-size:12px;line-height:1.55;color:var(--text);margin-top:8px}

/* footer */
.site-footer{position:absolute;top:3688px;left:0;width:1200px;height:316px;background:var(--dark);color:#ddd}
.footer-brand{position:absolute;left:140px;top:86px;font-family:"Rajdhani",sans-serif;font-weight:700;font-size:32px;color:#fff;text-transform:uppercase;line-height:1.05;display:flex;align-items:center;gap:12px}
.footer-brand .dot{width:20px;height:20px;border-radius:50%;background:#fff}
.contact-block{position:absolute;display:flex;gap:14px}
.contact-block h4{font-size:14px;color:#fff;font-weight:700;text-transform:uppercase;letter-spacing:1px}
.contact-block p{font-size:12px;line-height:1.6;color:#bbb;margin-top:4px}
.divider{position:absolute;left:770px;top:70px;width:1px;height:140px;background:#444}
.socials{position:absolute;left:500px;top:176px;display:flex;gap:10px}
.socials i{width:26px;height:26px;border:1px solid #fff;border-radius:50%}
.copyright{position:absolute;left:0;bottom:26px;width:100%;text-align:center;font-size:12px;color:#aaa}
</style>
</head>
<body>

<header class="site-header">
  <div class="topbar">
    <span><svg width="13" height="13" viewBox="0 0 24 24"><path d="M6 2l4 4-2 3a12 12 0 0 0 7 7l3-2 4 4-3 4C10 22 2 14 2 5z" fill="#1b1b1b"/></svg>Call Us : +1 612 555 0148</span>
    <span><svg width="14" height="12" viewBox="0 0 24 18"><rect x="1" y="1" width="22" height="16" fill="none" stroke="#1b1b1b" stroke-width="2"/><path d="M1 1l11 9 11-9" fill="none" stroke="#1b1b1b" stroke-width="2"/></svg>Email : hello@velkmfg.com</span>
  </div>
  <div class="brand"><span class="dot"></span>Velk Manufacturing</div>
  <nav class="main-nav"><span>Home</span><span>TREMLA Product</span><span>About Us</span><span>Capabilities</span><span>Contact</span></nav>
</header>

<section class="hero">
  <div class="hero-photo" role="img" aria-label="Close-up of a heap of dark machined metal parts"></div>
  <div class="hero-content">
    <h1 class="hero-title"><span class="line1">VELK</span><span class="line2">MANUFACTURING</span></h1>
    <span class="btn-green">Get in touch</span>
  </div>
  <div class="hero-dots"><i class="on"></i><i></i><i></i></div>
  <svg class="hero-wave" width="1200" height="120" viewBox="0 0 1200 120">
    <path d="M0 20 Q600 150 1200 20 L1200 120 L0 120Z" fill="#fff"/>
    <path d="M0 20 Q600 150 1200 20" fill="none" stroke="#59FF00" stroke-width="6"/>
  </svg>
</section>

<section class="why">
  <h2 class="heading section-title">Why Velk Manufacturing?</h2>
  <p class="lead">Because there is a better way, and we will find it, even if it's the hard way. We believe in working harder and smarter to achieve success.</p>
  <div class="why-cards">
    <div class="why-card">
      <div class="icon"><svg width="44" height="44" viewBox="0 0 44 44" fill="none" stroke="#1b1b1b" stroke-width="2.5"><circle cx="20" cy="24" r="16"/><circle cx="20" cy="24" r="9"/><circle cx="20" cy="24" r="2" fill="#1b1b1b"/><path d="M20 24L38 6M32 6h6v6"/></svg></div>
      <p>Our success is measured in your success</p>
    </div>
    <div class="why-card">
      <div class="icon"><svg width="44" height="44" viewBox="0 0 44 44" fill="none" stroke="#1b1b1b" stroke-width="2.5"><path d="M6 20h7v18H6zM13 22l7-14c3 0 4 2 3 6l-1 5h12c3 0 4 2 3 5l-3 10c-1 3-3 4-5 4H13"/></svg></div>
      <p>Focused on our your needs &amp; making excellent parts</p>
    </div>
    <div class="why-card">
      <div class="icon"><svg width="44" height="44" viewBox="0 0 44 44" fill="none" stroke="#1b1b1b" stroke-width="2.5"><circle cx="22" cy="22" r="17"/><circle cx="16" cy="18" r="1.5" fill="#1b1b1b"/><circle cx="28" cy="18" r="1.5" fill="#1b1b1b"/><path d="M14 26q8 8 16 0"/></svg></div>
      <p>Exceeding your expectations</p>
    </div>
  </div>
</section>

<section class="featured">
  <h2 class="heading section-title">Featured Product</h2>
  <p class="sub">Sed ut perspiciatis unde omnis iste natus error sit voluptatem accusantium doloremque</p>
  <div class="product-row">
    <svg class="arrow left" width="20" height="60" viewBox="0 0 20 60"><path d="M18 2L2 30l16 28" fill="none" stroke="#999" stroke-width="2"/></svg>
    <div class="product-card"><div class="product-photo" role="img" aria-label="Rows of brass machined fittings"></div><div class="stars">★★★★★</div><h3 class="heading product-name">Product Name</h3><span class="btn-outline">View details</span></div>
    <div class="product-card"><div class="product-photo b" role="img" aria-label="Dark machined fixture with polished faces"></div><div class="stars">★★★★★</div><h3 class="heading product-name">Product Name</h3><span class="btn-outline">View details</span></div>
    <div class="product-card"><div class="product-photo c" role="img" aria-label="Green TREMLA tool in a fitted case"></div><div class="stars">★★★★★</div><h3 class="heading product-name">Product Name</h3><span class="btn-outline">View details</span></div>
    <div class="product-card"><div class="product-photo d" role="img" aria-label="Bronze blocks on a blue work surface"></div><div class="stars">★★★★★</div><h3 class="heading product-name">Product Name</h3><span class="btn-outline">View details</span></div>
    <svg class="arrow right" width="20" height="60" viewBox="0 0 20 60"><path d="M2 2l16 28L2 58" fill="none" stroke="#999" stroke-width="2"/></svg>
  </div>
</section>

<section class="process">
  <div class="process-photo" role="img" aria-label="Green anodized TREMLA tool with steel handle"></div>
  <div class="process-body">
    <h2 class="heading">How we make it better</h2>
    <div class="rule"></div>
    <ul>
      <li>With 100 years of combined knowledge and experience to draw upon, we find solutions.</li>
      <li>Our vast experience across multiple industries gives us insight that is invaluable in creativity and foresight.</li>
      <li>The real life experience brings a broader understanding of your needs, and more importantly, what doesn't work, ultimately allowing us to make more informed decisions.</li>
      <li>We consider the smallest details, and analyze all the ways to create a better product the first time.</li>
      <li>Its conspiracy runs deep, we see problems before they become issues.</li>
    </ul>
  </div>
</section>

<section class="gallery">
  <h2 class="heading section-title">Photo Gallery</h2>
  <p class="sub">Sed ut perspiciatis unde omnis iste natus error sit voluptatem accusantium doloremque</p>
  <div class="gallery-grid">
    <div class="g1" role="img" aria-label="Perforated round steel plate"></div>
    <div class="g2" role="img" aria-label="Tray of turned aluminium parts"></div>
    <div class="g3" role="img" aria-label="Dark coiled machined parts on blue"></div>
    <div class="g4" role="img" aria-label="Brass parts laid on a blue mat"></div>
    <div class="g5" role="img" aria-label="Grid of small finished components"></div>
    <div class="g6" role="img" aria-label="Polished metal fixture close-up"></div>
  </div>
</section>

<section class="capabilities">
  <h2 class="heading section-title">Capabilities</h2>
  <p class="sub" style="color:#333">Quest a lot.&nbsp; Take a look at the brief list below for more.</p>
  <div class="cap-grid">
    <div class="cap">
      <svg width="44" height="44" viewBox="0 0 44 44" fill="none" stroke="#1b1b1b" stroke-width="2"><circle cx="14" cy="12" r="6"/><path d="M4 38c0-8 4-14 10-14s10 6 10 14"/><circle cx="33" cy="26" r="6"/><path d="M33 16v4M33 32v4M23 26h4M39 26h4"/></svg>
      <h3 class="heading">Capabilities</h3>
      <p>While this list covers much of our capabilities, it is by no means exhaustive.</p>
    </div>
    <div class="cap">
      <svg width="44" height="44" viewBox="0 0 44 44" fill="none" stroke="#1b1b1b" stroke-width="2"><rect x="4" y="6" width="36" height="24"/><path d="M16 36h12M22 30v6M12 22l8-8 6 6 6-6"/></svg>
      <h3 class="heading">CAD Design</h3>
      <p>We use the latest 3D CAD modeling software to bring your ideas to life.</p>
    </div>
    <div class="cap">
      <svg width="44" height="44" viewBox="0 0 44 44" fill="none" stroke="#1b1b1b" stroke-width="2"><rect x="4" y="6" width="36" height="30" rx="2"/><path d="M4 13h36M14 22l-5 4 5 4M30 22l5 4-5 4M24 20l-4 12"/></svg>
      <h3 class="heading">CAM Programming</h3>
      <p>We use the latest 3D CAM programming software to make your designs.</p>
    </div>
    <div class="cap">
      <svg width="44" height="44" viewBox="0 0 44 44" fill="none" stroke="#1b1b1b" stroke-width="2"><rect x="4" y="4" width="36" height="36"/><path d="M4 12h36M18 12v8h8v-8M20 20l2 4 2-4M12 34h20"/></svg>
      <h3 class="heading">FFF 3D Printing</h3>
      <p>Using fused filament fabrication we can 3D print prototypes for evaluation.</p>
    </div>
  </div>
</section>

<footer class="site-footer">
  <div class="footer-brand"><span class="dot"></span><span>Velk<br>Manufacturing</span></div>
  <div class="contact-block" style="left:460px;top:76px">
    <svg width="18" height="22" viewBox="0 0 18 22"><path d="M9 21S1 12 1 8a8 8 0 0 1 16 0c0 4-8 13-8 13z" fill="#fff"/><circle cx="9" cy="8" r="3" fill="#0d0d0d"/></svg>
    <div><h4>Address</h4><p>4820 Birch Ridge Drive,<br>Plymouth, MN 55441</p></div>
  </div>
  <div class="socials"><i></i><i></i></div>
  <div class="divider"></div>
  <div class="contact-block" style="left:810px;top:76px">
    <svg width="18" height="18" viewBox="0 0 24 24"><path d="M6 2l4 4-2 3a12 12 0 0 0 7 7l3-2 4 4-3 4C10 22 2 14 2 5z" fill="#fff"/></svg>
    <div><h4>Phone</h4><p>+1 612 555 0148</p></div>
  </div>
  <div class="contact-block" style="left:810px;top:160px">
    <svg width="18" height="14" viewBox="0 0 24 18"><rect x="1" y="1" width="22" height="16" fill="none" stroke="#fff" stroke-width="2"/><path d="M1 1l11 9 11-9" fill="none" stroke="#fff" stroke-width="2"/></svg>
    <div><h4>Email</h4><p>hello@velkmfg.com</p></div>
  </div>
  <p class="copyright">© 2020 Velk Manufacturing All rights reserved.</p>
</footer>

</body>
</html>
```